Packaging Design Project

PLEASE NOTE: YOU MUST USE ADOBE ILLUSTRATOR FOR THIS PROJECT.
I need a design for a plastic bag packaging for our product, Dustraline. Please see the website for more information about the product we sell, www.greenwise-home-supply.example
Colours to use are red, green and yellow of various tones and shades.
The dimensions of the bag are approximately: 20cm wide by 25cm high with a 3.5 to 4 cm side width.
Front of Bag
Must have the company logo – please see attached file A1 Q.pdf. Please separate this label in two. i.e. the company logo is only the part that says Greenwise Home Supply (with the green heartbeat design)
Also must have the product logo/signage – see the file A1 Q.pdf (attached). Please delete the Pty Ltd after the company name.
Must have product information: according to these words: “easy to use, safe around pets and children, non toxic, no chemicals”
The upper top of the bag must have the words: “resealable pack: cut here to start your cleaner, kinder future.”
The front of the bag also must have a picture relating to the product - plant and/or animal picture. Please see the website for more ideas of what pictures you can include. www.greenwise-home-supply.example. The picture must be large and take up most of the front of the bag. It must be eye catching, being the first thing the customers see.
Must have the following words somewhere on the front of the bag
• No more pests
• No more chemicals
• No more worries
• Pet friendly
Also must include: “Controls fleas, flea larvae and flea eggs: bedbugs: lice and mites: flies and biting flies: hookworm, roundworm and tapeworms”
Front must also include: KTR certification, Product of Australia, Glenhaven company logo, approximately 2 x 2 cm
Front, back and sides of bag should have the quantity amount
Sides of bag must have company name and product name
Back of bag
Must have 1 small paragraph about the company. See attached file Company Background.doc
1 small paragraph about congratulating customer for buying a clean safe effective product.- this has to be the dominant feature of the back of the bag. It must be large and eye catching
1 paragraph about Dustraline and how it works. – also included in the file Company Background.doc.
Must have an analysis of what's in the product – please see attached file
Must include rates of application – please see attached file Rates of Application.doc
Back of bag must include company logo somewhere – leave space for this
must include safety directions and barcode –please see attached file Safety Directions.doc
Updates
Forgot to tell you all that the design has to be done in Adobe Illustrator Version 10 and above. Thanks!
Reason: Hi Everyone
The project has been extended by 2 days. Keep all those designs coming in!
Hi Designers,
Here is an update to the brief which I think will make your lives easier!
Update/Changes
The dimensions of the bag are confirmed to be 21cm wide by 29cm high.
Please delete the previous information and change it to the following:
Controls fleas, bedbugs, lice, mites, flies, biting flies, hookworm, roundworm and tapeworm in pets.
Controls aphids, mealy bugs, harlequin bugs, white fly and cabbage aphids on plants.
Please put the following words under the product label, under the word "Dustraline":
Active Constituents:900g/kg amorphous silica
The safety directions has changed. It should now read:
Safety Directions
May irritate eyes and skin. Avoid contact with eyes and skin. Do not inhale dust. Wash hands after use.
Please note:
In the file we uploaded, the Dustraline label had a heartbeat line which ended with "Greenwise Home Supply....etc. Somehow everyone has lost this beepy line. Please put back the beepy line on
the Dustraline word.

```html
<!DOCTYPE html>
<html lang="en">
<head>
<meta charset="utf-8">
<title>Dustraline – Bag Side Panel</title>
<link rel="stylesheet" href="https://fonts.googleapis.com/css2?family=Source+Sans+3:wght@400;700&display=swap">
<style>
  :root {
    --panel-bg: #f8f9f8;
    --label-green: #2fe200;
    --label-text: #f3f7c6;
    --ink: #111111;
  }
  html, body {
    margin: 0;
    padding: 0;
    width: 1200px;
    height: 3785px;
    overflow: hidden;
    background: var(--panel-bg);
  }
  .side-panel {
    position: relative;
    width: 1200px;
    height: 3785px;
    background: var(--panel-bg);
    font-family: "Source Sans 3", "Myriad Pro", Arial, sans-serif;
  }
  .product-label {
    position: absolute;
    left: 0;
    top: 1315px;
    width: 1178px;
    height: 1153px;
    background: var(--label-green);
  }
  .product-label__text {
    position: absolute;
    left: 510px;
    top: 20px;
    height: 1110px;
    writing-mode: vertical-rl;
    transform: rotate(180deg);
    color: var(--label-text);
    text-align: start;
  }
  .product-name {
    display: block;
    font-size: 212px;
    font-weight: 400;
    line-height: 0.95;
    letter-spacing: 1px;
  }
  .company-name {
    display: block;
    font-size: 100px;
    font-weight: 400;
    line-height: 1.1;
    margin-right: 18px;
  }
  .quantity {
    position: absolute;
    left: 50px;
    top: 2540px;
    margin: 0;
    font-size: 78px;
    color: var(--ink);
    line-height: 1;
  }
  .quantity__label {
    font-weight: 700;
  }
  .quantity__value {
    font-weight: 400;
    font-size: 66px;
  }
</style>
</head>
<body>
  <main class="side-panel">
    <section class="product-label">
      <div class="product-label__text">
        <span class="product-name">Dustraline</span>
        <span class="company-name">Greenwise Home Supply</span>
      </div>
    </section>
    <p class="quantity"><span class="quantity__label">Quantity</span><span class="quantity__value">...xxxxxxx</span></p>
  </main>
</body>
</html>
```